marcello's mobile mechanic

a business card that will get attention from clients
- name of the business: M'S MOBILE MECHANIC
- we currently do not have a logo and do not need one at the moment, happy for the designers to just put the business name on the card using appropriate fonts

Target Market(s)

low cost mobile repairs

Industry/Entity Type

Business

Contact Information for Business Card

attracts customers

Font styles to use
Sans Serif

Colors
0255a3
fbee3d
000000

Requirements
Must have
• (555) 381-7094
• Marcello Treviske
• for lower income target market
Nice to have
• "we save you money"
• Easy to read
Should not have
• nothing comes to mind

```html
<!DOCTYPE html>
<html lang="en">
<head>
<meta charset="utf-8">
<title>M'S Mobile Mechanic — Business Card</title>
<link rel="stylesheet" href="https://fonts.googleapis.com/css2?family=Oswald:wght@500&family=Montserrat:wght@400;600&display=swap">
<style>
  :root {
    --brand-blue: #0255a3;
    --brand-blue-deep: #02488c;
    --brand-yellow: #fbee3d;
    --brand-yellow-shade: #d8cd2a;
    --brand-black: #000000;
    --backdrop: #e9e9ea;
    --text-light: #ffffff;
    --text-soft: #d6e2f1;
  }
  * { box-sizing: border-box; margin: 0; padding: 0; }
  html, body {
    width: 1200px;
    height: 904px;
    overflow: hidden;
    background: var(--backdrop);
  }
  .stage {
    width: 1200px;
    height: 904px;
    display: flex;
    flex-direction: column;
    align-items: center;
    justify-content: center;
    gap: 60px;
  }
  .card {
    position: relative;
    width: 620px;
    height: 354px;
    border-radius: 18px;
    overflow: hidden;
    box-shadow: 0 10px 26px rgba(0, 0, 0, 0.22);
  }
  .card__band {
    position: absolute;
    left: 0;
    right: 0;
    bottom: 0;
    height: 16px;
    background: var(--brand-yellow);
    border-top: 2px solid var(--brand-yellow-shade);
  }

  /* Front: personal side */
  .card--front {
    background: linear-gradient(160deg, var(--brand-blue) 0%, var(--brand-blue-deep) 100%);
    color: var(--text-light);
    text-align: center;
  }
  .card__name {
    position: absolute;
    top: 128px;
    left: 0;
    right: 0;
    font-family: "Oswald", sans-serif;
    font-weight: 500;
    font-size: 40px;
    letter-spacing: 0.5px;
    text-transform: uppercase;
  }
  .card__contact {
    position: absolute;
    top: 248px;
    left: 0;
    right: 0;
    font-family: "Montserrat", sans-serif;
  }
  .card__phone {
    font-weight: 600;
    font-size: 15px;
    letter-spacing: 0.3px;
  }
  .card__tagline {
    margin-top: 2px;
    font-weight: 400;
    font-size: 17px;
    color: var(--text-soft);
  }

  /* Back: business side */
  .card--back {
    background: var(--brand-black);
    display: flex;
    align-items: center;
    justify-content: center;
  }
  .card__business {
    font-family: "Montserrat", sans-serif;
    font-weight: 600;
    font-size: 30px;
    color: var(--text-light);
    letter-spacing: 1px;
    white-space: nowrap;
    margin-bottom: 16px;
  }
</style>
</head>
<body>
  <main class="stage">
    <section class="card card--front" aria-label="Business card front">
      <h1 class="card__name">Marcello Treviske</h1>
      <div class="card__contact">
        <p class="card__phone">(555) 381-7094</p>
        <p class="card__tagline">for lower income target market</p>
      </div>
      <div class="card__band"></div>
    </section>

    <section class="card card--back" aria-label="Business card back">
      <h2 class="card__business">M'S MOBILE MECHANIC</h2>
      <div class="card__band"></div>
    </section>
  </main>
</body>
</html>
```